Body therapist needs a business card

I need a card for my business which is teaching trainings in body therapy, the company is called Wexcombe Educational Group. I teach to massage therapists around Australia, South East Asia and the USA. I am attaching my logo which will guide you as to what colours I would like to have you consider. Please consult my website to find out more about what I do. www.corvantela.com.au

My name is Daniel Wexcombe. My phone number is (03) 9417 2608 or 0461753208. email is info@corvantela.com.au

```html
<!DOCTYPE html>
<html lang="en">
<head>
<meta charset="utf-8">
<title>Wexcombe Educational Group – Business Card</title>
<link rel="stylesheet" href="https://fonts.googleapis.com/css2?family=Poppins:wght@400;500&display=swap">
<style>
  :root {
    --stage: #2a2a2a;
    --card: #dddcdb;
    --card-shade: #cfcecd;
    --pattern-light: #d8d7d6;
    --pattern-dark: #c6c5c5;
    --ink: #1f1f1f;
    --accent: #e30613;
  }
  * { box-sizing: border-box; margin: 0; padding: 0; }
  html, body {
    width: 1200px; height: 960px; overflow: hidden;
    background: var(--stage);
    font-family: "Poppins", sans-serif;
    color: var(--ink);
  }
  .stage {
    width: 1200px; height: 960px;
    display: flex; flex-direction: column;
    align-items: center; justify-content: center; gap: 40px;
  }
  .card {
    position: relative;
    width: 760px; height: 434px;
    border-radius: 30px;
    background: var(--card);
    overflow: hidden;
  }

  /* Front */
  .brand {
    position: absolute; left: 60px; top: 200px;
    display: flex; align-items: center; gap: 14px;
    font-size: 20px; font-weight: 500; color: var(--ink);
  }
  .brand-dot {
    width: 22px; height: 22px; border-radius: 50%;
    background: var(--accent); flex: none;
  }
  .person {
    position: absolute; left: 400px; top: 110px;
    font-size: 32px; font-weight: 400; letter-spacing: 0.5px;
    white-space: nowrap;
  }
  .person .first { color: var(--accent); }
  .contacts {
    position: absolute; left: 420px; top: 170px;
    list-style: none;
    display: flex; flex-direction: column; gap: 8px;
    font-size: 17px; letter-spacing: 0.3px;
  }
  .contacts li { display: flex; align-items: center; gap: 10px; }
  .contacts svg { width: 18px; height: 18px; flex: none; }
  .footer-line {
    position: absolute; left: 40px; right: 24px; bottom: 44px;
    display: flex; align-items: center; gap: 10px;
  }
  .web-small { font-size: 17px; white-space: nowrap; letter-spacing: 0.3px; }
  .web .name { color: var(--accent); }
  .rule { flex: 1; height: 2px; background: var(--ink); }
  .rule-dot { width: 14px; height: 14px; border-radius: 50%; background: var(--accent); flex: none; }
  .rule-tail { width: 30px; height: 2px; background: var(--ink); flex: none; }

  /* Back */
  .pattern-field {
    position: absolute; inset: 0;
    background: radial-gradient(circle at 50% 45%, var(--pattern-light), var(--pattern-dark));
  }
  .back-content {
    position: absolute; inset: 0;
    display: flex; flex-direction: column;
    align-items: center; justify-content: center; gap: 46px;
  }
  .back .brand {
    position: static; font-size: 26px;
  }
  .back .brand-dot { width: 28px; height: 28px; }
  .web-large { font-size: 44px; letter-spacing: 0.5px; }
</style>
</head>
<body>
<main class="stage">

  <section class="card front">
    <div class="brand"><span class="brand-dot"></span>Wexcombe Educational Group</div>

    <h1 class="person"><span class="first">Daniel</span> Wexcombe</h1>

    <ul class="contacts">
      <li>
        <svg viewBox="0 0 18 18" aria-hidden="true"><circle cx="9" cy="9" r="9" fill="var(--accent)"/><path d="M5.5 6.2c.3 2.9 3.1 5.8 6.2 6.3l1-1.4-1.6-1-.8.8c-1-.5-1.9-1.4-2.4-2.4l.8-.8-1-1.6z" fill="#fff"/></svg>
        0461753208
      </li>
      <li>
        <svg viewBox="0 0 18 18" aria-hidden="true"><circle cx="9" cy="9" r="9" fill="var(--accent)"/><path d="M5.5 6.2c.3 2.9 3.1 5.8 6.2 6.3l1-1.4-1.6-1-.8.8c-1-.5-1.9-1.4-2.4-2.4l.8-.8-1-1.6z" fill="#fff"/></svg>
        (03) 9417 2608
      </li>
      <li>
        <svg viewBox="0 0 18 18" aria-hidden="true"><circle cx="9" cy="9" r="9" fill="var(--accent)"/><rect x="4.5" y="6" width="9" height="6.5" fill="#fff"/><path d="M4.5 6l4.5 3.6L13.5 6" fill="none" stroke="var(--accent)" stroke-width="1"/></svg>
        info@corvantela.com.au
      </li>
    </ul>

    <div class="footer-line">
      <span class="web web-small">www.<span class="name">corvantela</span>.com.au</span>
      <span class="rule"></span>
      <span class="rule-dot"></span>
      <span class="rule-tail"></span>
    </div>
  </section>

  <section class="card back">
    <div class="pattern-field" role="img" aria-label="Soft grey repeating brand-mark pattern covering the card background"></div>
    <div class="back-content">
      <div class="brand"><span class="brand-dot"></span>Wexcombe Educational Group</div>
      <p class="web web-large">www.<span class="name">corvantela</span>.com.au</p>
    </div>
  </section>

</main>
</body>
</html>
```